Infographic Design for Aluminium Can Recycling

We require a neat design that can be integrated into print advertising for a 'cash for cans' recycling promotion and also scaled back for Chatterloop promotion. The promotion is aimed at kids/families. Needs to be fresh and colourful - but also appealing to children. The flyer is to be designed at A5 size and also at CL post sizing. You can just submit the one design in A5 to win, with the knowledge that you will need to redesign slightly later to suit CL post size.

The design needs to contain as much of the following as possible.

- The best thing is - Aluminium is 100% recyclable FOREVER
- If you recycled just one can everyday for a week, you'd save enough energy to watch TV straight for 21 hours - thats an entire season of XXX
- 105,784 cans are recycled every minute
- it takes the same amount of energy to make 1 new can as it does to recycle 20
- a recycled can is back on the shelf in 60 days
-2/3 of the aluminium ever produced is still in use today

Please keep colours muted - not bright
Please do not present anything like the 'Blue Lantern' lie attached. This is far too busy.
I have attached the original flyer for information only (see below for what to and what NOT to include)
I've attached some cute graphics I think kids and adults will find appealing. Design something similar. The prize to be won is an electric scooter - perhaps they could be riding this.

They are giving away an electric Scooter (not Bike)

Please use Penbury Ore Services and LOGO

Please provide address and details of event as per flyer

Please leave out the following text:
HEY KIDS
WIN THIS BIKE
FIND US ON CL
LUCKY DOOR PRIZE + SAUSAGE SIZZLE
WE PAY CASH FOR CANS
Collect as many aluminium cans as you can and bring them to our can day and get paid for cash
Do not include the can man graphic

Please have information:
Event location
Win an Electric Scooter
Turn in your CANS for CASH

Great - can't wait to see what you creative geniuses come back with!!
Updates

None of these designs matched the brief. Im actually not sure what to do now?

Target Market(s)

Males 35+

Industry/Entity Type

Advertising

Font styles to use
Sans Serif

Colors
5c5c5c
0555a3
3276b5
b1b1b1
faa54b
fbf289
33a6d7
f04a50

Requirements
Must have
• Please read brief
Nice to have
• Please see brief
Should not have
• Please see brief

```html
<!DOCTYPE html>
<html lang="en">
<head>
<meta charset="utf-8">
<title>Turn in your Cans for Cash – Penbury Ore Services</title>
<link href="https://fonts.googleapis.com/css2?family=Lobster+Two:ital,wght@1,700&family=Open+Sans:ital,wght@0,400;0,700;1,400&display=swap" rel="stylesheet">
<style>
  :root {
    --page: #ffffff;
    --navy: #0b40d4;
    --sky: #45c9f1;
    --sky-deep: #35b9ef;
    --band: #0c3fcf;
    --yellow: #f4ef6a;
    --red: #e8202a;
    --white: #ffffff;
    --logo-blue: #1c58d8;
    --silver-light: #e8eaec;
    --silver-dark: #5e6266;
  }
  * { box-sizing: border-box; margin: 0; padding: 0; }
  html, body { width: 900px; height: 1200px; overflow: hidden; background: var(--page); }
  .flyer {
    position: absolute; left: 38px; top: 18px; width: 822px; height: 1163px;
    background: var(--sky); overflow: hidden;
  }
  .sky-wave { position: absolute; left: 0; top: 0; width: 822px; height: 320px; }
  .headline {
    position: absolute; left: 37px; top: 28px;
    font-family: "Lobster Two", cursive; font-weight: 700; font-style: italic;
    font-size: 54px; line-height: 60px; color: var(--yellow);
  }
  .can-visual {
    position: absolute; left: 478px; top: 14px; width: 320px; height: 440px;
    border-radius: 40px;
    background: radial-gradient(ellipse at 45% 40%, var(--silver-light) 0%, #a9adb1 45%, var(--silver-dark) 100%);
  }
  .prize-visual {
    position: absolute; left: 22px; top: 220px; width: 380px; height: 310px;
    clip-path: polygon(50% 0, 60% 25%, 88% 8%, 76% 38%, 100% 48%, 76% 60%, 86% 92%, 58% 74%, 48% 100%, 40% 74%, 14% 98%, 22% 62%, 0 52%, 22% 40%, 6% 10%, 36% 26%);
    background: radial-gradient(circle at 50% 50%, #fbf6a0 0%, var(--yellow) 70%);
  }
  .prize-callout {
    position: absolute; left: 212px; top: 300px;
    transform: rotate(-16deg); transform-origin: left top;
    font-family: "Lobster Two", cursive; font-weight: 700; font-style: italic;
    font-size: 34px; line-height: 40px; color: var(--red); text-align: center;
    text-shadow: 2px 2px 0 var(--yellow), -2px -2px 0 var(--yellow), 2px -2px 0 var(--yellow), -2px 2px 0 var(--yellow);
  }
  .facts {
    position: absolute; left: 22px; top: 542px; width: 785px; list-style: none;
    font-family: "Open Sans", sans-serif; font-size: 21.5px; line-height: 40px; color: var(--white);
  }
  .facts li { position: relative; padding-left: 23px; margin-bottom: 4px; text-align: justify; }
  .facts li::before {
    content: ""; position: absolute; left: 0; top: 14px; width: 12px; height: 12px;
    border-radius: 50%; background: var(--white);
  }
  .facts .note { padding-left: 23px; margin-top: -2px; margin-bottom: 4px; }
  .facts .note::before { display: none; }
  .event {
    position: absolute; left: 0; top: 907px; width: 822px; height: 208px; background: var(--sky-deep);
  }
  .brand { position: absolute; left: 78px; top: 40px; width: 200px; text-align: center; }
  .brand-mark { width: 90px; height: 90px; margin: 0 auto 14px; border-radius: 50%; background: var(--logo-blue); }
  .brand-name {
    font-family: "Open Sans", sans-serif; font-weight: 700; font-size: 17px; line-height: 20px;
    color: var(--logo-blue); text-transform: uppercase;
  }
  .details {
    position: absolute; left: 385px; top: 38px;
    font-family: "Open Sans", sans-serif; font-weight: 700; font-size: 20.5px; line-height: 38px; color: var(--white);
  }
  .details dt { display: inline-block; width: 70px; }
  .details dd { display: inline; }
  .details dd::after { content: ""; display: block; }
  .prize-draw {
    position: absolute; left: 0; bottom: 0; width: 822px; height: 48px; background: var(--band);
    font-family: "Open Sans", sans-serif; font-style: italic; font-size: 31px; line-height: 48px;
    color: var(--white); text-align: center;
  }
</style>
</head>
<body>
<main class="flyer">
  <svg class="sky-wave" viewBox="0 0 822 320" aria-hidden="true">
    <path d="M0 0H822V282C700 250 560 200 380 185C220 172 90 180 0 198Z" fill="var(--navy)"/>
  </svg>
  <h1 class="headline">Turn in your<br>CANS for CASH</h1>
  <div class="can-visual" role="img" aria-label="Large crushed silver aluminium drink can"></div>
  <div class="prize-visual" role="img" aria-label="Yellow starburst with a child riding a red electric scooter"></div>
  <p class="prize-callout">Win an<br>Electric Scooter</p>

  <ul class="facts">
    <li>The best thing is - Aluminium is 100% recyclable FOREVER</li>
    <li class="note">If you recycled just one can everyday for a week, you'd save Enough energy to watch TV straight for 21 hours - thats an entire season of XXX</li>
    <li>105,784 cans are recycled every minute</li>
    <li>It takes the same amount of energy to make 1 new can as it does to recycle 20</li>
    <li>A recycled can is back on the shelf in 60 days</li>
    <li>2/3 of the aluminium ever produced is still in use today</li>
  </ul>

  <section class="event">
    <div class="brand">
      <div class="brand-mark"></div>
      <p class="brand-name">Penbury Ore Services</p>
    </div>
    <dl class="details">
      <dt>When</dt><dd>: Satturday your Date</dd>
      <dt>Where</dt><dd>: 18 Larch St Northvale</dd>
      <dt>Time</dt><dd>: 8 am-12 pm</dd>
      <dt>Phone</dt><dd>: 02 5550 0147 or 1300 555 014</dd>
    </dl>
  </section>

  <p class="prize-draw">Lucky door prize will be drawn at 12 pm</p>
</main>
</body>
</html>
```